Halvorn spray foam and Environmental

I have business cards but need new ones. The ones I have are very bland. Here is. Y company website http://www.halvornsprayfoam.ca

Also I can send you copies of the current cards
I would also need my current logo on the new design as well.. Also spray foam and Environmental

Industry/Entity Type

Business

Logo Text

Halvorn.

```html
<!DOCTYPE html>
<html lang="en">
<head>
<meta charset="utf-8">
<title>Halvorn Spray Foam and Environmental – Business Card</title>
<link rel="stylesheet" href="https://fonts.googleapis.com/css2?family=Roboto:ital,wght@0,400;0,700;1,400&family=Roboto+Condensed:wght@400&family=Rubik:wght@400&display=swap">
<style>
  :root {
    --purple: #6f4189;
    --purple-text: #6b3a87;
    --grey: #c3c5c9;
    --grey-text: #8a8a8a;
    --dark-text: #555558;
    --white: #ffffff;
    --backdrop: #e7e4df;
  }
  * { box-sizing: border-box; margin: 0; padding: 0; }
  html, body { width: 900px; height: 1200px; overflow: hidden; }
  body { background: var(--backdrop); font-family: "Roboto", Arial, sans-serif; position: relative; }

  .card {
    position: absolute; left: 85px; width: 733px; height: 429px;
    background: var(--white); border-radius: 22px; overflow: hidden;
    box-shadow: 0 6px 16px rgba(0,0,0,.25);
  }
  .card--front { top: 143px; }
  .card--back { top: 633px; }
  .card__waves { position: absolute; left: 0; top: 0; width: 733px; height: 429px; }

  /* Front: brand lockup */
  .brand { position: absolute; left: 135px; top: 62px; width: 448px; height: 102px; }
  .brand__square { position: absolute; left: 0; top: 0; width: 123px; height: 101px; background: var(--purple); border-radius: 5px; }
  .brand__rule { position: absolute; left: 141px; top: 2px; width: 2px; height: 98px; background: #cfcfcf; }
  .brand__text { position: absolute; right: 0; top: 0; text-align: right; }
  .brand__tagline { font-style: italic; font-size: 17px; color: var(--grey-text); line-height: 1; }
  .brand__name { font-weight: 700; font-size: 64px; color: var(--purple-text); line-height: 1; margin-top: 2px; letter-spacing: 0.5px; }
  .brand__descriptor { font-family: "Roboto Condensed", "Arial Narrow", sans-serif; font-size: 20px; color: var(--dark-text); line-height: 1; margin-top: 2px; }

  /* Front: contacts */
  .contact { position: absolute; top: 296px; color: var(--white); }
  .contact--spray { left: 63px; }
  .contact--enviro { left: 413px; }
  .contact__title { font-weight: 700; font-size: 20px; letter-spacing: .3px; margin-bottom: 10px; }
  .contact__line { display: flex; align-items: center; font-family: "Rubik", Arial, sans-serif; font-size: 16px; height: 23px; }
  .contact__line svg { width: 14px; height: 14px; margin-right: 8px; flex: none; }
  .contact-divider { position: absolute; left: 355px; top: 300px; width: 1px; height: 92px; background: rgba(255,255,255,.55); }

  /* Back: services */
  .services { position: absolute; color: var(--purple-text); }
  .services--spray { left: 92px; top: 86px; }
  .services--enviro { left: 373px; top: 87px; }
  .services__kicker { font-size: 21px; line-height: 1; }
  .services__title { font-weight: 700; font-size: 31px; line-height: 1; margin: 4px 0 9px; }
  .services__list { list-style: none; font-family: "Rubik", Arial, sans-serif; font-size: 17px; }
  .services__list li { height: 23px; display: flex; align-items: center; }
  .services__list li::before { content: ""; width: 6px; height: 6px; border-radius: 50%; background: var(--purple-text); margin-right: 9px; }
</style>
</head>
<body>

<section class="card card--front" aria-label="Card front">
  <svg class="card__waves" viewBox="0 0 733 429" aria-hidden="true">
    <path fill="var(--purple)" d="M0,165 C170,225 360,240 733,190 L733,429 L0,429 Z"/>
    <path fill="var(--white)" d="M0,198 C210,262 420,205 733,255 L733,272 C430,228 220,292 0,230 Z"/>
    <path fill="var(--grey)" d="M0,208 C210,268 420,214 733,258 L733,264 C425,222 215,282 0,222 Z"/>
  </svg>

  <div class="brand">
    <div class="brand__square"></div>
    <div class="brand__rule"></div>
    <div class="brand__text">
      <p class="brand__tagline">Residential &amp; Commercial</p>
      <p class="brand__name">HALVORN</p>
      <p class="brand__descriptor">Spray foam and Environmental</p>
    </div>
  </div>

  <div class="contact contact--spray">
    <p class="contact__title">SPRAY FOAM</p>
    <p class="contact__line"><svg viewBox="0 0 16 16"><path fill="#fff" d="M3 2h3l1 3-2 1.5a8 8 0 0 0 4.5 4.5L11 9l3 1v3a1 1 0 0 1-1 1A12 12 0 0 1 2 3a1 1 0 0 1 1-1z"/></svg>604-555-0148</p>
    <p class="contact__line"><svg viewBox="0 0 16 16"><rect x="1" y="3" width="14" height="10" fill="#fff"/><path d="M1 3l7 6 7-6" fill="none" stroke="var(--purple)" stroke-width="1.3"/></svg>halvornfoam@halvornmail.ca</p>
    <p class="contact__line"><svg viewBox="0 0 16 16"><g fill="none" stroke="#fff" stroke-width="1.3"><circle cx="8" cy="8" r="6.5"/><ellipse cx="8" cy="8" rx="3" ry="6.5"/><path d="M1.5 8h13M2.5 4.5h11M2.5 11.5h11"/></g></svg>www.halvornsprayfoam.ca</p>
  </div>

  <div class="contact-divider"></div>

  <div class="contact contact--enviro">
    <p class="contact__title">ENVIRONMENTAL</p>
    <p class="contact__line"><svg viewBox="0 0 16 16"><path fill="#fff" d="M3 2h3l1 3-2 1.5a8 8 0 0 0 4.5 4.5L11 9l3 1v3a1 1 0 0 1-1 1A12 12 0 0 1 2 3a1 1 0 0 1 1-1z"/></svg>604-555-0192</p>
    <p class="contact__line"><svg viewBox="0 0 16 16"><rect x="1" y="3" width="14" height="10" fill="#fff"/><path d="M1 3l7 6 7-6" fill="none" stroke="var(--purple)" stroke-width="1.3"/></svg>enviro1@halvornmail.ca</p>
    <p class="contact__line"><svg viewBox="0 0 16 16"><g fill="none" stroke="#fff" stroke-width="1.3"><circle cx="8" cy="8" r="6.5"/><ellipse cx="8" cy="8" rx="3" ry="6.5"/><path d="M1.5 8h13M2.5 4.5h11M2.5 11.5h11"/></g></svg>www.halvornenvironmental.ca</p>
  </div>
</section>

<section class="card card--back" aria-label="Card back">
  <svg class="card__waves" viewBox="0 0 733 429" aria-hidden="true">
    <path fill="var(--purple)" d="M0,318 C200,360 430,350 733,308 L733,429 L0,429 Z"/>
    <path fill="var(--white)" d="M0,335 C220,405 450,330 733,360 L733,382 C450,350 220,425 0,362 Z"/>
    <path fill="var(--grey)" d="M0,345 C220,410 450,338 733,364 L733,374 C450,346 220,418 0,356 Z"/>
  </svg>

  <div class="services services--spray">
    <p class="services__kicker">HALVORN</p>
    <p class="services__title">SPRAY FOAM</p>
    <ul class="services__list">
      <li>Roofing Foam</li>
      <li>Slabjacking</li>
      <li>2 pound / half pound</li>
      <li>Sound proofing</li>
      <li>Batt insulation</li>
      <li>Attic Blow in</li>
    </ul>
  </div>

  <div class="services services--enviro">
    <p class="services__kicker">HALVORN</p>
    <p class="services__title">ENVIRONMENTAL</p>
    <ul class="services__list">
      <li>Air monitoring</li>
      <li>Asbestos testing</li>
      <li>Asbestos removal</li>
      <li>Building demolition</li>
      <li>Lead testing</li>
      <li>Mould removal</li>
    </ul>
  </div>
</section>

</body>
</html>
```